Mortgage Broking boutique Business

I’m wanting a revamped look to my existing business card design. I do like the black and silver but happy to have other colours introduced based on your creation. I’ve attached a copy of my current card so you can have a starting point updated details noted brloe. I deal with high net worth individuals so need my card to be sophisticated, classy that gives off a classy vibe

Target Market(s)

High net worth, wealthy

Industry/Entity Type

Mortgage Brokerage

Contact Information for Business Card

Job title: Finance Executive
Phone: +61 7 3287 4419
Mobile: 0471 352 608
Email: marcus@quillbrookcapital.com.au
Web: www.quillbrookcapital.com.au
Address: level 36 Tindale Court, 58 Harwick St Brisbane QLD 4000

Font styles to use
Other font styles liked:
• Helvetica

Colors

Designer to choose colors to be used in the design.

Requirements
Must have
• Use my existing card design as a starting point

```html
<!DOCTYPE html>
<html lang="en">
<head>
<meta charset="utf-8">
<title>Quillbrook Capital — Business Card</title>
<link href="https://fonts.googleapis.com/css2?family=Jost:wght@400;500;600&display=swap" rel="stylesheet">
<style>
  :root {
    --backdrop: #4b4c4c;
    --card: #1d1d1d;
    --silver: #d8d8d8;
    --silver-soft: #bdbdbd;
    --name-grey: #8c8c8c;
    --rule: #5a5a5a;
    --icon: #8f8f8f;
  }
  * { margin: 0; padding: 0; box-sizing: border-box; }
  html, body {
    width: 963px; height: 1200px; overflow: hidden;
    background: var(--backdrop);
    font-family: "Jost", "Futura", sans-serif;
  }
  .card {
    position: absolute; left: 232px;
    width: 558px; height: 316px;
    background: var(--card);
  }
  .card--front { top: 222px; }
  .card--back { top: 636px; }

  /* front */
  .brand-frame {
    position: absolute; left: 57px; top: 109px;
    width: 197px; height: 102px;
    border: 2px solid var(--silver-soft);
    display: flex; align-items: center; justify-content: center;
  }
  .brand-frame::after {
    content: ""; position: absolute; inset: 4px;
    border: 1px solid var(--silver-soft);
  }
  .brand-name {
    color: var(--silver); font-weight: 500;
    font-size: 11px; letter-spacing: 2.5px; text-align: center; line-height: 1.35;
  }
  .divider {
    position: absolute; left: 281px; top: 80px;
    width: 1px; height: 161px; background: var(--rule);
  }
  .details { position: absolute; left: 304px; top: 78px; color: var(--silver); }
  .person-name { font-size: 22px; font-weight: 600; color: var(--name-grey); line-height: 1.1; }
  .job-title { font-size: 14px; margin-top: 2px; }
  .address { font-size: 13px; line-height: 17px; margin-top: 10px; }
  .contacts { list-style: none; margin-top: 10px; font-size: 13px; }
  .contacts li { display: flex; align-items: center; height: 17.5px; }
  .contacts svg { width: 11px; height: 11px; margin-right: 10px; fill: var(--icon); flex: none; }

  /* back */
  .back-frame {
    position: absolute; left: 17px; top: 16px; right: 17px; bottom: 18px;
    border: 2px solid var(--silver-soft);
    display: flex; align-items: center; justify-content: center;
  }
  .back-brand {
    color: var(--silver); font-weight: 500;
    font-size: 22px; letter-spacing: 4px; text-align: center; line-height: 1.3;
  }
</style>
</head>
<body>
  <section class="card card--front">
    <div class="brand-frame">
      <p class="brand-name">QUILLBROOK<br>CAPITAL</p>
    </div>
    <div class="divider"></div>
    <div class="details">
      <h1 class="person-name">MARCUS VERITY</h1>
      <p class="job-title">Finance Executive</p>
      <p class="address">level 36 Tindale Court<br>58 Harwick St Brisbane QLD 4000</p>
      <ul class="contacts">
        <li><svg viewBox="0 0 16 16" aria-hidden="true"><path d="M3 1l3 3-1.5 2c1 2 3 4 5 5L11.5 9.5l3 3-2 2.5C6 14 1.5 9 1 3z"/></svg>+61 7 3287 4419</li>
        <li><svg viewBox="0 0 16 16" aria-hidden="true"><path d="M4 0h8v16H4zM5.5 2v10h5V2zM7 13.3h2v1.4H7z" fill-rule="evenodd"/></svg>0471 352 608</li>
        <li><svg viewBox="0 0 16 16" aria-hidden="true"><path d="M1 3h14v10H1zM2 4l6 5 6-5" fill-rule="evenodd"/></svg>marcus@quillbrookcapital.com.au</li>
        <li><svg viewBox="0 0 16 16" aria-hidden="true"><path d="M8 1a7 7 0 100 14A7 7 0 008 1zM3 6h4v3H5zM9 4h3l1 4-3 1-1 3H8z" fill-rule="evenodd"/></svg>www.quillbrookcapital.com.au</li>
      </ul>
    </div>
  </section>

  <section class="card card--back">
    <div class="back-frame">
      <p class="back-brand">QUILLBROOK<br>CAPITAL</p>
    </div>
  </section>
</body>
</html>
```